Website Design for a New Business Sharing Application

Purpose: Website for a new product – a sharing application called "Gathr.io"

Product concept: Easy sharing of business information. The application has different sections: tasks, calendars, documents, contacts, notes and links. The key feature of the application is that you can drag and drop information from different sections into a "share." A share is a page which lists all the types of information that you drag into it. You can add people to this "share."

Note: The application itself is not part of this project, just the website.

Website details: The site, in addition to being informational, will actually be the first point of entry for visitors into the application itself. Because of that, we would like the website design to reflect the look of the application, to create a smooth and seamless experience for the user moving from the website into the application (tough the website does not need to look *exactly* like the application). Included Product Tour screenshots show you the look of the application.

Website pages to be created: 4 pages
We are flexible in terms of the exact structure and placement of elements. You may change that any way you like. The pages are as follows:

Home page
Product Tour page
Press page
Blog page

Specific description of pages are provided in project files we will upload. We will also upload the logo, home page layout we have in mind, and other supporting files.

NOTE: Please submit first the design of the home page. Based on this design we will ask selected designers to submit designs for the other pages.

Target Market(s)

Business people who want to share work related files with their colleagues

Industry/Entity Type

Business

Requirements
Must have
• All the required features are listed in the description of the website and specific pages that we will upload.

```html
<!DOCTYPE html>
<html lang="en">
<head>
<meta charset="utf-8">
<title>Gathr.io – Share NOW</title>
<link href="https://fonts.googleapis.com/css2?family=Ubuntu:wght@400;500;700&display=swap" rel="stylesheet">
<style>
  :root {
    --page-bg: #f3efe4;
    --rust: #d2581a;
    --rust-text: #cf5a20;
    --amber: #e48a0b;
    --panel-bg: #f7f3ea;
    --brand-blue: #2a7bbf;
    --btn-top: #3d97d8;
    --btn-bottom: #1f6fb2;
    --white: #ffffff;
    --input-border: #c9c4b8;
  }
  * { box-sizing: border-box; margin: 0; padding: 0; }
  html, body { width: 1200px; height: 862px; overflow: hidden; }
  body {
    position: relative;
    background: var(--page-bg);
    font-family: "Ubuntu", Arial, sans-serif;
  }
  .top-band { position: absolute; left: 0; top: 0; width: 1200px; height: 12px; background: var(--rust); }

  .brand { position: absolute; left: 42px; top: 44px; display: flex; align-items: center; gap: 12px; }
  .brand-dot { width: 40px; height: 40px; border-radius: 50%; background: var(--rust); }
  .brand-name { font-size: 46px; font-weight: 500; color: var(--brand-blue); line-height: 1; }

  .top-links { position: absolute; right: 72px; top: 30px; font-family: Arial, Helvetica, sans-serif; font-size: 16px; color: var(--rust); }
  .top-links a { color: var(--rust); text-decoration: none; }
  .top-links .sep { margin: 0 14px; }

  .tagline { position: absolute; left: 0; width: 1172px; top: 117px; text-align: center; font-size: 34px; color: var(--rust-text); }
  .headline { position: absolute; left: 0; width: 1216px; top: 170px; text-align: center; font-size: 53px; font-weight: 500; color: var(--rust-text); }

  .share-panel { position: absolute; left: 37px; top: 254px; width: 606px; height: 386px; background: var(--panel-bg); box-shadow: 0 1px 3px rgba(0,0,0,.18); }
  .share-panel-head { height: 73px; background: var(--amber); color: var(--white); font-size: 33px; padding: 16px 0 0 25px; }
  .share-panel-foot { position: absolute; left: 0; bottom: 0; width: 100%; height: 30px; background: var(--amber); }
  .share-types { position: absolute; left: 53px; top: 108px; list-style: none; font-size: 19px; color: var(--brand-blue); line-height: 29px; }
  .share-arrow { position: absolute; left: 217px; top: 196px; }
  .share-target { position: absolute; left: 322px; top: 160px; display: flex; align-items: center; gap: 12px; opacity: .3; }
  .share-target .brand-dot { width: 46px; height: 46px; }
  .share-target .brand-name { font-size: 44px; }

  .or-badge { position: absolute; left: 676px; top: 444px; width: 50px; height: 50px; background: var(--rust); color: var(--white); font-size: 33px; text-align: center; line-height: 48px; }

  .signup-label { position: absolute; left: 744px; top: 362px; font-size: 32px; color: var(--rust); }
  .email-field { position: absolute; left: 742px; top: 415px; width: 415px; height: 36px; background: #f6f3ec; border: 1px solid var(--input-border); border-radius: 3px; box-shadow: inset 0 1px 2px rgba(0,0,0,.1); }

  .btn { position: absolute; height: 48px; background: linear-gradient(var(--btn-top), var(--btn-bottom)); color: var(--white); border: 1px solid #1a5f99; border-radius: 2px; font-size: 22px; display: flex; align-items: center; }
  .btn-start { left: 910px; top: 485px; width: 247px; padding-left: 36px; font-size: 24px; gap: 12px; }
  .btn-about { left: 43px; top: 686px; width: 247px; padding-left: 30px; }
  .btn-video { left: 300px; top: 686px; width: 247px; padding-left: 26px; }

  .site-footer { position: absolute; left: 0; top: 778px; width: 1200px; height: 84px; background: var(--rust); }
  .footer-nav { position: absolute; left: 37px; top: 18px; font-size: 15px; color: var(--white); white-space: nowrap; }
  .footer-nav .sep { margin: 0 10px; }
  .pricing-note { position: absolute; left: 276px; top: 45px; width: 134px; text-align: center; font-family: Arial, Helvetica, sans-serif; font-size: 12px; line-height: 14px; color: var(--white); }
  .pricing-note::before { content: ""; display: block; width: 54px; height: 1px; background: var(--white); margin: 0 auto 5px; }
  .social { position: absolute; right: 40px; top: 24px; display: flex; gap: 12px; }
  .social-item { display: flex; align-items: center; gap: 4px; font-size: 12px; color: var(--white); }
  .social-item i { width: 12px; height: 12px; background: var(--white); display: block; }
</style>
</head>
<body>
  <div class="top-band"></div>

  <header>
    <div class="brand"><span class="brand-dot"></span><span class="brand-name">Gathr.io</span></div>
    <nav class="top-links"><a href="#">Link1</a><span class="sep">|</span><a href="#">Link2</a><span class="sep">|</span><a href="#">Link3</a></nav>
  </header>

  <p class="tagline">Certified fastest sharing in the market. Its social.</p>
  <h1 class="headline">Share NOW</h1>

  <section class="share-panel">
    <div class="share-panel-head">Drag information, add people BOOM!</div>
    <ul class="share-types">
      <li>&gt; Files</li><li>&gt; Pictures</li><li>&gt; Tasks</li><li>&gt; To-dos</li><li>&gt; Calendars</li><li>&gt; Notes</li><li>&gt; Links</li>
    </ul>
    <svg class="share-arrow" width="44" height="36" viewBox="0 0 44 36"><path d="M0 0 L44 18 L0 36 L10 18 Z" fill="#2a86cc"/></svg>
    <div class="share-target"><span class="brand-dot"></span><span class="brand-name">Gathr.io</span></div>
    <div class="share-panel-foot"></div>
  </section>

  <div class="or-badge">or</div>

  <h2 class="signup-label" style="font-weight:400">Enter business email</h2>
  <div class="email-field"></div>
  <div class="btn btn-start">Start sharing
    <svg width="26" height="16" viewBox="0 0 26 16"><path d="M1 8 H23 M16 2 L23 8 L16 14" stroke="#fff" stroke-width="2.6" fill="none"/></svg>
  </div>

  <div class="btn btn-about">What is it ?</div>
  <div class="btn btn-video">Watch video</div>

  <footer class="site-footer">
    <nav class="footer-nav">Home<span class="sep">|</span>About us<span class="sep">|</span>Product Tour<span class="sep">|</span>Pricing<span class="sep">|</span>Terms of use<span class="sep">|</span>Jobs<span class="sep">|</span>Sign up<span class="sep">|</span>Blog<span class="sep">|</span>Press<span class="sep">|</span>Contact us</nav>
    <div class="pricing-note">FREE FOR<br>UNLIMITED USERS</div>
    <div class="social">
      <span class="social-item"><i></i>Linkup</span>
      <span class="social-item"><i></i>Chirper</span>
      <span class="social-item"><i></i>Plusone</span>
    </div>
  </footer>
</body>
</html>
```